Outdoor mass notification company needing business card design.

Our company name is Harborline Signal Systems Inc located in Amory Mississippi and we sell and maintain "Corvath" Mass Notification Sirens in the US. Outdoor sirens notify people of certain severe dangers such as tornados, severe thunderstorms, flooding, hurricanes and tsunamis. We also serve the oil and gas refining industries to warn of Chemical releases, fires, and lightning alerts.

Contact Information for Business Card

Name, title, cell number, email address

Requirements
Nice to have
• The Corvath logo and also the Tallbrook logo.

```html
<!DOCTYPE html>
<html lang="en">
<head>
<meta charset="UTF-8">
<title>Harborline Signal Systems – Business Card</title>
<link rel="stylesheet" href="https://fonts.googleapis.com/css2?family=Merriweather:wght@700;900&family=Arimo:wght@400;700&display=swap">
<style>
  :root {
    --navy: #34536f;
    --navy-dark: #2a4560;
    --ink: #1d1d1f;
    --paper: #ffffff;
    --stage: #e9ebee;
    --siren-dark: #2a2a2c;
    --siren-light: #9a9ca0;
  }
  * { box-sizing: border-box; margin: 0; padding: 0; }
  html, body { width: 1200px; height: 780px; overflow: hidden; }
  body {
    background: var(--stage);
    display: flex;
    align-items: center;
    justify-content: center;
    gap: 60px;
    font-family: "Arimo", Arial, sans-serif;
  }

  /* Front: portrait contact card */
  .card-front {
    position: relative;
    width: 380px;
    height: 620px;
    background: var(--paper);
    border-radius: 26px;
    box-shadow: 0 10px 30px rgba(0,0,0,.15);
    overflow: hidden;
  }
  .front-wordmark {
    position: absolute;
    top: 48px;
    left: 34px;
    right: 30px;
    font-family: "Merriweather", Georgia, serif;
    font-weight: 900;
    color: var(--navy);
    text-transform: uppercase;
    line-height: 1.1;
  }
  .front-wordmark .line-1 { display: block; font-size: 30px; letter-spacing: .5px; }
  .front-wordmark .line-2 { display: block; font-size: 21px; letter-spacing: 1px; }
  .identity {
    position: absolute;
    top: 150px;
    left: 0;
    padding-left: 34px;
  }
  .identity::before {
    content: "";
    position: absolute;
    left: 0;
    top: 2px;
    width: 18px;
    height: 30px;
    background: var(--navy);
  }
  .person-name {
    font-weight: 700;
    font-size: 24px;
    color: var(--navy);
    letter-spacing: .5px;
    text-transform: uppercase;
  }
  .person-title {
    font-size: 16px;
    color: var(--ink);
    margin-top: 4px;
  }
  .address {
    font-size: 17px;
    color: var(--ink);
    margin-top: 16px;
    line-height: 1.35;
  }
  .contact-list {
    list-style: none;
    margin-top: 14px;
    font-size: 17px;
    color: var(--ink);
    line-height: 1.45;
  }
  .contact-list li { display: flex; align-items: center; gap: 8px; white-space: nowrap; }
  .contact-list svg { width: 14px; height: 14px; fill: var(--navy); flex: none; }
  .siren-photo {
    position: absolute;
    right: 0;
    bottom: 0;
    width: 160px;
    height: 165px;
    background: linear-gradient(160deg, var(--siren-dark) 0%, var(--siren-light) 55%, var(--siren-dark) 100%);
    border-top-left-radius: 12px;
  }

  /* Back: landscape brand card */
  .card-back {
    width: 620px;
    height: 380px;
    background: var(--navy);
    border-radius: 30px;
    box-shadow: 0 6px 0 var(--navy-dark), 0 14px 30px rgba(0,0,0,.2);
    display: flex;
    align-items: center;
    justify-content: center;
  }
  .back-wordmark {
    font-family: "Merriweather", Georgia, serif;
    font-weight: 900;
    color: var(--paper);
    text-transform: uppercase;
    text-align: center;
    line-height: 1.15;
  }
  .back-wordmark .line-1 { display: block; font-size: 50px; letter-spacing: 1px; }
  .back-wordmark .line-2 { display: block; font-size: 36px; letter-spacing: 2px; }
</style>
</head>
<body>

  <section class="card-front">
    <h1 class="front-wordmark">
      <span class="line-1">Harborline</span>
      <span class="line-2">Signal Systems</span>
    </h1>

    <div class="identity">
      <p class="person-name">Daniel Reese</p>
      <p class="person-title">Managing Director</p>
      <p class="address">Your address, City<br>State, Zip 1234</p>
      <ul class="contact-list">
        <li>
          <svg viewBox="0 0 24 24" aria-hidden="true"><path d="M6.6 10.8a15 15 0 0 0 6.6 6.6l2.2-2.2a1 1 0 0 1 1-.25 11.4 11.4 0 0 0 3.6.57 1 1 0 0 1 1 1V20a1 1 0 0 1-1 1A17 17 0 0 1 3 4a1 1 0 0 1 1-1h3.5a1 1 0 0 1 1 1c0 1.25.2 2.45.57 3.57a1 1 0 0 1-.25 1z"/></svg>
          123 456 789
        </li>
        <li>
          <svg viewBox="0 0 24 24" aria-hidden="true"><path d="M3 5h18v14H3zm2 2v.5l7 4.5 7-4.5V7zm0 2.9V17h14V9.9l-7 4.5z"/></svg>
          info@yourmail.com
        </li>
        <li>
          <svg viewBox="0 0 24 24" aria-hidden="true"><circle cx="12" cy="12" r="10"/></svg>
          www.yourwebsite.com
        </li>
      </ul>
    </div>

    <div class="siren-photo" role="img" aria-label="Photo of an outdoor mass notification siren array mounted on a pole"></div>
  </section>

  <section class="card-back">
    <h2 class="back-wordmark">
      <span class="line-1">Harborline</span>
      <span class="line-2">Signal Systems</span>
    </h2>
  </section>

</body>
</html>
```